Design a Business Card from pre-existing logo

I have a logo for my company and am looking for a designer to design the business card
I have a basic idea of what i want but new ideas are welcome too!

Am attaching a reference of the front side and the logo to be used.
the front will have a logo and the company name, the back will have a name, designation, phone number , website in very elegant font and clean formatting .... you can experiment with icons if you like(font and background colour needs to match front).

the font on the front needs to be chosen too !
i will need the illustrator/photoshop file too, for later customisation or updating..

```html
<!DOCTYPE html>
<html lang="en">
<head>
<meta charset="utf-8">
<title>Orla Studio – Business Card</title>
<link href="https://fonts.googleapis.com/css2?family=Montserrat:wght@400;500;700&family=Quicksand:wght@500;600&display=swap" rel="stylesheet">
<style>
  :root {
    --backdrop: #26282c;
    --yellow-base: #f0b51e;
    --yellow-mid: #f5c624;
    --yellow-light: #fbe03a;
    --yellow-deep: #e8a91a;
    --ink: #2b2b2b;
    --ink-soft: #4a4a4a;
  }
  * { margin: 0; padding: 0; box-sizing: border-box; }
  html, body { width: 1200px; height: 900px; overflow: hidden; }
  body {
    background: var(--backdrop);
    position: relative;
    font-family: "Quicksand", sans-serif;
  }
  .card {
    position: absolute;
    top: 295px;
    width: 540px;
    height: 310px;
    overflow: hidden;
    background: var(--yellow-base);
  }
  .card--front { left: 40px; }
  .card--back { left: 620px; }
  .card__facets { position: absolute; inset: 0; width: 100%; height: 100%; }

  .logo-window {
    position: absolute;
    left: 190px; top: 75px;
    width: 160px; height: 160px;
    display: flex; align-items: center; justify-content: center;
    gap: 8px;
  }
  .logo-window__mark {
    width: 14px; height: 14px;
    border-radius: 50%;
    background: var(--ink);
    flex: none;
  }
  .logo-window__name {
    font-family: "Montserrat", sans-serif;
    font-weight: 700;
    font-size: 17px;
    color: var(--ink);
    white-space: nowrap;
  }

  .contact {
    position: absolute;
    left: 36px; top: 58px;
    color: var(--ink);
  }
  .contact__person { display: flex; gap: 10px; align-items: flex-start; margin-bottom: 10px; }
  .contact__name {
    font-family: "Montserrat", sans-serif;
    font-weight: 700;
    font-size: 17px;
    letter-spacing: 0.5px;
    line-height: 1;
  }
  .contact__role {
    font-family: "Montserrat", sans-serif;
    font-weight: 500;
    font-size: 9px;
    letter-spacing: 0.6px;
    margin-top: 3px;
  }
  .contact__list { list-style: none; }
  .contact__item {
    display: flex; align-items: center; gap: 10px;
    font-size: 12px; font-weight: 600;
    height: 22px;
    color: var(--ink-soft);
  }
  .contact__icon { width: 16px; height: 16px; flex: none; }
  .contact__dot { width: 10px; height: 10px; border-radius: 50%; background: var(--ink-soft); margin: 0 3px; flex: none; }

  .brand {
    position: absolute;
    right: 40px; top: 140px;
    font-family: "Montserrat", sans-serif;
    font-weight: 700;
    font-size: 22px;
    color: var(--ink);
    white-space: nowrap;
  }
</style>
</head>
<body>

<section class="card card--front" aria-label="Card front">
  <svg class="card__facets" viewBox="0 0 540 310" aria-hidden="true">
    <rect width="540" height="310" fill="var(--yellow-base)"/>
    <polygon points="0,0 540,0 350,75 190,75" fill="var(--yellow-mid)"/>
    <polygon points="0,0 190,75 190,235 0,310" fill="var(--yellow-deep)"/>
    <polygon points="540,0 540,310 350,235 350,75" fill="var(--yellow-base)"/>
    <polygon points="0,310 190,235 350,235 540,310" fill="var(--yellow-deep)" opacity="0.7"/>
    <rect x="190" y="75" width="160" height="160" fill="var(--yellow-light)"/>
  </svg>
  <div class="logo-window">
    <span class="logo-window__mark"></span>
    <span class="logo-window__name">Orla Studio</span>
  </div>
</section>

<section class="card card--back" aria-label="Card back">
  <svg class="card__facets" viewBox="0 0 540 310" aria-hidden="true">
    <rect width="540" height="310" fill="var(--yellow-deep)"/>
    <polygon points="0,0 320,0 260,310 0,310" fill="var(--yellow-base)"/>
    <polygon points="0,0 320,0 230,200 0,120" fill="var(--yellow-mid)"/>
    <polygon points="60,0 320,0 240,140" fill="var(--yellow-light)" opacity="0.8"/>
  </svg>

  <div class="contact">
    <div class="contact__person">
      <svg class="contact__icon" viewBox="0 0 16 16" aria-hidden="true">
        <circle cx="8" cy="5" r="3.2" fill="none" stroke="var(--ink)" stroke-width="1.3"/>
        <path d="M2 15c0-3.5 2.7-5.5 6-5.5s6 2 6 5.5" fill="none" stroke="var(--ink)" stroke-width="1.3"/>
      </svg>
      <div>
        <p class="contact__name">MARA QUINN</p>
        <p class="contact__role">CREATIVE DESIGNER</p>
      </div>
    </div>
    <ul class="contact__list">
      <li class="contact__item">
        <svg class="contact__icon" viewBox="0 0 16 16" aria-hidden="true">
          <path d="M4 2l2.5 3-1.5 1.5c.8 1.8 2.2 3.2 4 4l1.5-1.5 3 2.5-1.5 2.5C7 13.5 2.5 9 1.5 3.5z" fill="none" stroke="var(--ink-soft)" stroke-width="1.3" stroke-linejoin="round"/>
        </svg>
        <span>(0044) 555 0192 337</span>
      </li>
      <li class="contact__item">
        <svg class="contact__icon" viewBox="0 0 16 16" aria-hidden="true">
          <circle cx="8" cy="8" r="6.5" fill="none" stroke="var(--ink-soft)" stroke-width="1.3"/>
          <ellipse cx="8" cy="8" rx="2.8" ry="6.5" fill="none" stroke="var(--ink-soft)" stroke-width="1.1"/>
          <line x1="1.5" y1="8" x2="14.5" y2="8" stroke="var(--ink-soft)" stroke-width="1.1"/>
        </svg>
        <span>www.orla-studio.com</span>
      </li>
      <li class="contact__item">
        <span class="contact__dot"></span>
        <span>/orla_studio</span>
      </li>
    </ul>
  </div>

  <p class="brand">Orla Studio</p>
</section>

</body>
</html>
```